Flyer für ein Singer-Songwriter Festival
Vielen Dank für die Geduld und die schnellen Änderungen. Ich bin sehr zufrieden mit dem Ergebnis und freue mich auf die weitere Zusammenarbeit!
Zielgruppe
Wir sind ein gemeinnütziger Verein und unterstützen Kunst und Kulturschafende. Im November veranstalten wir ein Singer-Songwriter Festival. Es heißt: TideLark Korven Folkwave Festival. Im letzten Jahr fand das erste Festival statt und richtet sich an Newcommer aus Der Bereich Singer Songwriter und Kulturliebhaber bzw. Festivalgänger
Das Festival findet vom 28. November bis 29. November 2025 statt. Am ersten Abend findet der Contest der Newcomer statt der zweite Abend ist der 'Konzertabend' an dem die Jury und der / die Gewinnerin des Contest den Abend mit bestreiten werden.
Diese Informationen sollten auf die Rückseite des Flyers. Der Button 'Wir suchen dich' sollte ebenfalls auf die Rückseite.
ICON Pixora & Chatterly bitte einfügen.
Gefördert wird das Festival von der TULPA-Stiftung und der Konrad Wessel & Ida Marquardt-Stiftung (Varnek) dies sollte auf dem Flyer erwähnt werden
Aufgabenstellung
Ansprechend für junge Leute. Es gibt ein Logo und auch ein gestaltetes Plakat aus dem letzten Jahr. Postkartengröße für den Flyer.
DINA 4 Plakate

```html
<!DOCTYPE html>
<html lang="de">
<head>
<meta charset="utf-8">
<title>TideLark Korven Folkwave Festival – Flyer</title>
<link rel="stylesheet" href="https://fonts.googleapis.com/css2?family=Josefin+Sans:ital,wght@0,400;0,600;0,700;1,600&family=Didact+Gothic&family=Montserrat:wght@800;900&family=Oswald:wght@600&display=swap">
<style>
  :root {
    --stage: #e6e6e6;
    --orange: #e55a27;
    --sky: #acd8db;
    --ink: #2c3539;
    --white: #ffffff;
    --stone: #b3b7b3;
    --red: #e2231a;
    --coin: #d9dbdc;
  }
  * { box-sizing: border-box; margin: 0; padding: 0; }
  html, body { width: 997px; height: 1200px; overflow: hidden; background: var(--stage); }
  .stage { position: relative; width: 997px; height: 1200px; }

  .flyer { position: absolute; top: 87px; width: 360px; height: 1018px; overflow: hidden; background: var(--sky); }
  .flyer--front { left: 102px; }
  .flyer--back { left: 528px; }

  .abs { position: absolute; left: 0; width: 100%; }
  .center { text-align: center; }

  /* front */
  .front__head { top: 0; height: 136px; background: var(--orange); }
  .front__skyline-top { top: 136px; height: 86px; background: linear-gradient(var(--orange), var(--sky)); }
  .front__title { top: 22px; font-family: "Josefin Sans", sans-serif; font-style: italic; font-weight: 600; font-size: 36px; color: var(--white); letter-spacing: -0.5px; }
  .front__subtitle { top: 68px; font-family: "Josefin Sans", sans-serif; font-style: italic; font-weight: 600; font-size: 18px; line-height: 23px; color: var(--white); }

  .festival-name { font-family: "Oswald", sans-serif; font-weight: 600; color: var(--ink); text-transform: uppercase; line-height: 1.1; }
  .front__name { top: 420px; font-size: 40px; }
  .back__name { top: 150px; font-size: 34px; }

  .social { font-family: "Josefin Sans", sans-serif; font-weight: 600; font-size: 12.5px; color: var(--ink); letter-spacing: -0.2px; }
  .social span + span { margin-left: 8px; }
  .front__social { top: 618px; }
  .back__social { top: 30px; }

  .front__skyline-bottom { top: 700px; height: 127px; background: linear-gradient(var(--sky), var(--white)); }
  .front__badge { position: absolute; left: 206px; top: 712px; width: 98px; height: 98px; border-radius: 50%; background: var(--coin); }
  .front__lower { top: 827px; bottom: 0; background: var(--white); }
  .front__info { top: 837px; font-family: "Josefin Sans", sans-serif; font-weight: 700; font-size: 12px; color: var(--red); letter-spacing: -0.3px; }
  .dates { font-family: "Didact Gothic", sans-serif; color: var(--ink); }
  .front__dates { top: 872px; left: 26px; width: 320px; font-size: 46px; line-height: 46px; letter-spacing: -1px; }
  .venue { font-family: "Didact Gothic", sans-serif; font-size: 19px; color: var(--ink); }
  .front__venue { top: 978px; left: 27px; }

  /* back */
  .back__badge { position: absolute; left: 138px; top: 283px; width: 194px; height: 194px; border-radius: 50%; background: var(--stone); text-align: center; font-family: "Montserrat", sans-serif; }
  .back__badge-title { margin-top: 30px; font-weight: 900; font-size: 24px; line-height: 23px; color: var(--white); }
  .back__badge-text { margin-top: 6px; font-weight: 800; font-size: 11.5px; line-height: 14px; color: var(--ink); }
  .back__skyline { top: 470px; height: 66px; background: linear-gradient(var(--sky), var(--white)); }
  .back__lower { top: 536px; height: 372px; background: var(--white); }
  .back__event { left: 34px; width: auto; }
  .back__day { font-size: 68px; line-height: 60px; letter-spacing: -1px; }
  .back__label { font-family: "Didact Gothic", sans-serif; font-size: 29px; color: var(--orange); margin-top: 6px; }
  .back__event--1 { top: 592px; }
  .back__event--2 { top: 721px; }
  .back__venue { top: 840px; left: 31px; font-size: 18px; }
  .back__footer { top: 908px; bottom: 0; background: var(--orange); color: var(--white); font-family: "Josefin Sans", sans-serif; font-weight: 700; font-size: 11.5px; }
  .back__footer-head { margin-top: 28px; }
  .back__footer-list { margin-top: 16px; line-height: 15px; }
</style>
</head>
<body>
<main class="stage">

  <section class="flyer flyer--front">
    <div class="abs front__head"></div>
    <div class="abs front__skyline-top" role="img" aria-label="Silhouette der Lübecker Altstadt-Skyline in Orange"></div>
    <h1 class="abs center front__title">WIR SUCHEN DICH!</h1>
    <p class="abs center front__subtitle">Bewirb dich jetzt bei unserem<br>Singer-Songwriter Contest</p>

    <p class="abs center festival-name front__name">TideLark Korven<br>Folkwave Festival</p>

    <p class="abs center social front__social"><span>PIXORA</span><span>CHATTERLY</span><span>TIDELARKKORVENFOLKWAVE</span></p>

    <div class="abs front__skyline-bottom" role="img" aria-label="Weiße Silhouette der Lübecker Kirchtürme"></div>
    <div class="front__badge" role="img" aria-label="Plakette des Fördervereins"></div>
    <div class="abs front__lower"></div>
    <p class="abs center front__info">ALLE INFOS UNTER WWW.KLANGMUENZE-LUEBECK.DE</p>
    <p class="abs dates front__dates">28.-29.<br>November 2025</p>
    <p class="abs venue front__venue">Veranstaltungsort — 23552 Lübeck</p>
  </section>

  <section class="flyer flyer--back">
    <p class="abs center social back__social"><span>PIXORA</span><span>CHATTERLY</span><span>TIDELARKKORVENFOLKWAVE</span></p>

    <p class="abs center festival-name back__name">TideLark Korven<br>Folkwave Festival</p>

    <div class="abs back__skyline" role="img" aria-label="Weiße Silhouette der Lübecker Altstadt"></div>
    <div class="abs back__lower"></div>

    <div class="back__badge">
      <p class="back__badge-title">WIR<br>SUCHEN<br>DICH!</p>
      <p class="back__badge-text">BEWIRB DICH JETZT<br>BEI UNSEREM<br>SINGER-SONGWRITER<br>CONTEST</p>
    </div>

    <div class="abs back__event back__event--1">
      <p class="dates back__day">28.11.</p>
      <p class="back__label">NEWCOMER-CONTEST</p>
    </div>
    <div class="abs back__event back__event--2">
      <p class="dates back__day">29.11.</p>
      <p class="back__label">KONZERTABEND</p>
    </div>
    <p class="abs venue back__venue">Veranstaltungsort — 23552 Lübeck</p>

    <footer class="abs center back__footer">
      <p class="back__footer-head">GEFÖRDERT DURCH:</p>
      <p class="back__footer-list">TULPA-Stiftung<br>Konrad Wessel &amp; Ida Marquardt-Stiftung (Varnek)</p>
    </footer>
  </section>

</main>
</body>
</html>
```